Melbourne Gym Celebrating 49 years of business

We are celebrating our 49th birthday and will be running a "12 month Membership Special" $299.00 save over 30%. Being one of the longest running gyms in the fitness industry the design must be very eye catching and professional in its appearance. Given the length of operation, artwork must also have a touch of class that will appeal to 18-40 year old's. Below are previous specials with its layout and sample 49th Anniversary layouts. The final design should emphasis the advertised sale, along with celebrating 49 years. You can be as creative as possible with layout and design.

Target Market(s)

Male and females aged between 18-40

Font styles to use
Serif
Sans Serif

Requirements
Must have
• Must emphasize either "Celebrating 49 years" "49th Anniversary" or Happy 49th Birthday" and in a large font "12 Month Special $299.00 SAVE OVER 30%" Terms and Conditions Apply, Strictly Limited Time Only.
• "contact details"
• Address: 14 Harlow Rd Tindale Park
• Ph: 9517 2860
• www.corvalfitness.com.au
• Design format must come in poster size A0 size, Instagram format, Facebook cover and 800 x 800 for the website
Nice to have
• Given the number of years in business, an elegant/classy feel would be nice to the overall presentation. Bright colors can be used along with artistic graphic designs

```html
<!DOCTYPE html>
<html lang="en">
<head>
<meta charset="utf-8">
<title>Corval Fitness – 49th Anniversary Poster</title>
<link rel="stylesheet" href="https://fonts.googleapis.com/css2?family=Bebas+Neue&display=swap">
<style>
  :root {
    --page-bg: #f2f2f2;
    --navy-deep: #151a2b;
    --navy-mid: #2b3350;
    --navy-light: #4a5476;
    --ink-white: #ffffff;
    --ring-grey: #8a8d99;
    --badge-fill: rgba(20, 22, 34, 0.72);
    --skin-warm: #8a6452;
    --kit-black: #1a1a1f;
  }
  * { margin: 0; padding: 0; box-sizing: border-box; }
  html, body {
    width: 1200px;
    height: 800px;
    overflow: hidden;
    background: var(--page-bg);
  }
  .poster {
    position: absolute;
    left: 333px;
    top: 21px;
    width: 534px;
    height: 758px;
    overflow: hidden;
    font-family: "Bebas Neue", "Arial Narrow", sans-serif;
    color: var(--ink-white);
  }
  .poster__backdrop {
    position: absolute;
    inset: 0;
    background:
      radial-gradient(ellipse at 35% 25%, var(--navy-light) 0%, transparent 55%),
      radial-gradient(ellipse at 70% 70%, var(--navy-mid) 0%, transparent 60%),
      linear-gradient(160deg, var(--navy-mid) 0%, var(--navy-deep) 100%);
  }
  .poster__athlete {
    position: absolute;
    left: 300px;
    top: 128px;
    width: 230px;
    height: 580px;
    border-radius: 110px 110px 20px 20px;
    background: linear-gradient(180deg, var(--skin-warm) 0%, #5d4337 45%, var(--kit-black) 70%, #111218 100%);
    opacity: 0.85;
  }
  .poster__header {
    position: absolute;
    top: 18px;
    left: 0;
    width: 100%;
    text-align: center;
    font-size: 26px;
    letter-spacing: 0.5px;
  }
  .headline__number {
    position: absolute;
    left: 45px;
    top: 112px;
    font-size: 222px;
    line-height: 1;
  }
  .headline__suffix {
    position: absolute;
    left: 223px;
    top: 120px;
    font-size: 90px;
    line-height: 1;
  }
  .headline__word {
    position: absolute;
    left: 47px;
    top: 296px;
    font-size: 88px;
    line-height: 1;
    letter-spacing: 0.5px;
  }
  .offer__title {
    position: absolute;
    left: 45px;
    top: 382px;
    font-size: 45px;
    line-height: 1;
    letter-spacing: -0.5px;
  }
  .offer__price {
    position: absolute;
    left: 45px;
    top: 423px;
    width: 223px;
    height: 51px;
    border: 2px solid var(--ink-white);
    text-align: center;
    font-size: 48px;
    line-height: 52px;
  }
  .savings-badge {
    position: absolute;
    left: 38px;
    top: 483px;
    width: 208px;
    height: 208px;
    border-radius: 50%;
    background: var(--badge-fill);
    border: 3px solid var(--ring-grey);
    text-align: center;
  }
  .savings-badge__label {
    display: block;
    margin-top: 37px;
    font-size: 42px;
    line-height: 1;
  }
  .savings-badge__value {
    display: block;
    font-size: 108px;
    line-height: 0.95;
  }
  .brand-name {
    position: absolute;
    left: 258px;
    top: 664px;
    width: 110px;
    text-align: center;
    font-size: 28px;
    line-height: 1;
  }
  .contact-bar {
    position: absolute;
    left: 44px;
    right: 34px;
    top: 728px;
    display: flex;
    justify-content: space-between;
    font-size: 14px;
    letter-spacing: 0.2px;
  }
</style>
</head>
<body>
  <main class="poster">
    <div class="poster__backdrop" role="img" aria-label="Dark navy grunge texture background"></div>
    <div class="poster__athlete" role="img" aria-label="Photo of a female athlete in black sportswear holding a dumbbell, looking over her shoulder"></div>

    <div class="poster__header">Corval Fitness</div>

    <div class="headline__number">49</div>
    <div class="headline__suffix">TH</div>
    <div class="headline__word">Anniversary</div>

    <div class="offer__title">12 Month Special</div>
    <div class="offer__price">$299.00</div>

    <div class="savings-badge">
      <span class="savings-badge__label">Save Over</span>
      <span class="savings-badge__value">30%</span>
    </div>

    <div class="brand-name">Corval Fitness</div>

    <footer class="contact-bar">
      <span>Address: 14 Harlow Rd Tindale Park</span>
      <span>Ph: 9517 2860</span>
      <span>www.corvalfitness.com.au</span>
    </footer>
  </main>
</body>
</html>
```